Business Card Design Project

We need a business card to reflect the design of our website - just so it all ties in - it has a retro feel and can be found at http://www.velorasoulpair.com
We will need our phone 0437 215 964
Web address, and email velorapair@fernmail.com included
Our catch cry is "Classic Cocktail Music"
Perfect Live Music for Private & Corporate Events, Weddings and Dinner Music
Our names should be included :-
Maribel Thorne / piano & Dennis Holloway / bass
I am now also including our logo so that it can be included (in part or whole) somehow in the design
My partner thinks we should include our logo in some form in the design of the card - i will attach this here for you. I will attach eps but if you prefer another format please let me know
Regards
Mari

```html
<!DOCTYPE html>
<html lang="en">
<head>
<meta charset="utf-8">
<title>Velora Pair – Business Card</title>
<link rel="stylesheet" href="https://fonts.googleapis.com/css2?family=Cinzel:wght@400;500&family=Open+Sans:wght@400;700&display=swap">
<style>
  :root {
    --backdrop: #333233;
    --card: #d9805f;
    --ink: #2b2624;
    --cream: #f0e3c6;
    --silhouette: #1b1918;
  }
  html, body {
    margin: 0;
    width: 1200px;
    height: 1000px;
    overflow: hidden;
    background: var(--backdrop);
  }
  .card {
    position: absolute;
    left: 51px;
    top: 201px;
    width: 1098px;
    height: 597px;
    background: var(--card);
    box-shadow: 0 6px 18px rgba(0,0,0,0.45);
  }
  .instrument-art {
    position: absolute;
    left: 27px;
    top: 9px;
    width: 273px;
    height: 578px;
    border-radius: 40px 40px 110px 110px;
    background: linear-gradient(180deg, #262322 0%, var(--silhouette) 100%);
  }
  .brand-name {
    position: absolute;
    left: 357px;
    top: 100px;
    margin: 0;
    font-family: "Cinzel", serif;
    font-weight: 400;
    font-size: 66px;
    letter-spacing: 3px;
    color: var(--cream);
    line-height: 1;
  }
  .tagline {
    position: absolute;
    left: 532px;
    top: 190px;
    margin: 0;
    font-family: "Open Sans", sans-serif;
    font-weight: 700;
    font-size: 28px;
    color: var(--ink);
    line-height: 1;
  }
  .members {
    position: absolute;
    left: 390px;
    top: 266px;
    width: 430px;
    margin: 0;
    text-align: center;
    font-family: "Cinzel", serif;
    font-weight: 500;
    font-size: 25px;
    line-height: 45px;
    color: var(--cream);
    text-shadow: 1px 1px 1px rgba(60,30,20,0.6);
    letter-spacing: 0.5px;
  }
  .contact {
    position: absolute;
    left: 640px;
    top: 440px;
    margin: 0;
    padding: 0;
    list-style: none;
    font-family: "Open Sans", sans-serif;
    font-size: 25px;
    line-height: 41px;
    color: var(--ink);
  }
  .contact b { font-weight: 700; }
</style>
</head>
<body>
  <div class="card">
    <div class="instrument-art" role="img" aria-label="Silhouette of an upright double bass whose body turns into piano keys"></div>
    <h1 class="brand-name">VELORA PAIR</h1>
    <p class="tagline">Classic Cocktail Music</p>
    <p class="members">
      Maribel Thorne / Piano<br>
      &amp;<br>
      Dennis Holloway / Bass
    </p>
    <ul class="contact">
      <li><b>phone:</b> 0437 215 964</li>
      <li><b>email:</b> velorapair@fernmail.com</li>
      <li><b>web:</b> www.velorasoulpair.com</li>
    </ul>
  </div>
</body>
</html>
```